A community driven app for reporting beach risks like bluebottles and jellyfish. Users report sightings of jellyfish, bluebottles, sharks or other beach hazards and receive XP and unlock badges if other users confirm their reports.

This is for a mock-up, not a full app.

We require:
Bluebottle/jellyfish themed stylised text for "Quorvy" for use in headings and logos.

A cute/kawaii mascot bluebottle or jellyfish with images/poses for:
- main logo, smiling/blushing
- shrugging
- demonstrating Australian sun advice "slip, slop, slap, seek, slide" (see photos)
- wearing a stethoscope/doctor costume for medical advice for stings.

A colour palette for the app, should be bright/beach themed.

4 background slides/scenes for the app, again cartoony and beach themed.

4 other cute/kawaii sea creature single images e.g: bluebottle, shark, stingray, seahorse, whale, octopus, etc. they must be in the same style as the main mascot.

A radar loading animation with simple jellyfish icons instead of dots.

No preferences on animal/mascot colours or gender.

```html
<!DOCTYPE html>
<html lang="en">
<head>
<meta charset="utf-8">
<title>Quorvy – App Screens</title>
<link href="https://fonts.googleapis.com/css2?family=Fredoka:wght@500;600&family=Quicksand:wght@500;600;700&display=swap" rel="stylesheet">
<style>
  :root {
    --stage: #939393;
    --sky: #55acd9;
    --card: #45a0ce;
    --card-ghost: #6db9e0;
    --wave-deep: #4aa3d3;
    --wave-light: #a4dbef;
    --wave-line: #8fcfee;
    --sand: #f2d07f;
    --sand-shade: #e6c06c;
    --sun: #f9cb3e;
    --white: #ffffff;
    --ink: #1f2a33;
    --props: #e9b95a;
    --mascot: #a9dcf3;
  }
  * { box-sizing: border-box; margin: 0; padding: 0; }
  html, body { width: 1200px; height: 823px; overflow: hidden; background: var(--stage); }
  .canvas { position: relative; width: 1200px; height: 823px; }

  .screen {
    position: absolute; top: 100px; width: 322px; height: 622px;
    background: var(--sky); overflow: hidden;
    box-shadow: 0 14px 40px rgba(0,0,0,.28);
  }
  .screen--welcome { left: 85px; }
  .screen--tips { left: 439px; }
  .screen--confirm { left: 793px; }

  .brand {
    position: absolute; left: 0; right: 0; text-align: center;
    font-family: "Fredoka", sans-serif; font-weight: 600; color: var(--white);
    font-size: 42px; letter-spacing: 1px; line-height: 1;
  }
  .screen--welcome .brand { top: 34px; }
  .screen--tips .brand, .screen--confirm .brand { top: 20px; }

  .card-ghost {
    position: absolute; background: var(--card-ghost); opacity: .55;
    border-radius: 34px; transform: rotate(-6deg);
  }
  .card {
    position: absolute; left: 26px; width: 270px;
    background: var(--card); border-radius: 32px;
  }
  .screen--welcome .card { top: 123px; height: 284px; }
  .screen--welcome .card-ghost { left: 18px; top: 112px; width: 290px; height: 300px; }
  .screen--tips .card, .screen--confirm .card { top: 79px; height: 430px; }
  .screen--tips .card-ghost, .screen--confirm .card-ghost { left: 20px; top: 62px; width: 292px; height: 450px; transform: rotate(-5deg); }

  .heading {
    position: absolute; left: 0; right: 0; text-align: center;
    font-family: "Fredoka", sans-serif; font-weight: 500; color: var(--white);
    line-height: 35px;
  }
  .screen--welcome .heading { top: 160px; font-size: 33px; line-height: 40px; }
  .screen--tips .heading, .screen--confirm .heading { top: 112px; font-size: 28px; }

  .lede {
    position: absolute; left: 40px; right: 40px; top: 252px; text-align: center;
    font-family: "Quicksand", sans-serif; font-weight: 500; color: var(--white);
    font-size: 18px; line-height: 28px;
  }
  .cta {
    position: absolute; left: 93px; top: 364px; width: 137px; height: 44px;
    border-radius: 22px; background: var(--sun); border: none;
    font-family: "Quicksand", sans-serif; font-weight: 700; font-size: 13px;
    letter-spacing: .5px; color: #2f8fcb;
    box-shadow: 2px 4px 0 rgba(20,80,120,.25);
  }

  .tip { position: absolute; height: 47px; }
  .tip-label {
    position: absolute; right: 0; top: 0; height: 47px; padding: 0 12px 0 26px;
    background: var(--white); border-radius: 12px;
    font-family: "Quicksand", sans-serif; font-weight: 700; font-size: 17px;
    color: var(--ink); line-height: 47px;
  }
  .tip-art {
    position: absolute; left: 0; top: -10px; width: 54px; height: 66px;
    border-radius: 27px; background: radial-gradient(circle at 50% 40%, var(--mascot), #6fc0e6);
  }
  .tip--slip { left: 44px; top: 211px; width: 115px; }
  .tip--slop { left: 166px; top: 211px; width: 113px; }
  .tip--slap { left: 40px; top: 303px; width: 119px; }
  .tip--seek { left: 166px; top: 303px; width: 113px; }
  .tip--slide { left: 97px; top: 395px; width: 122px; }

  .report-art {
    position: absolute; left: 56px; top: 191px; width: 212px; height: 158px;
    border-radius: 16px; background: linear-gradient(135deg, #e8f5fb, #7cc6ea 60%, #3a9fd1);
  }
  .hazards { position: absolute; left: 54px; top: 366px; width: 214px; list-style: none; }
  .hazard {
    position: relative; height: 31px; display: flex; align-items: center;
    border-bottom: 1px solid rgba(255,255,255,.18);
    font-family: "Quicksand", sans-serif; font-weight: 700; font-size: 15px; color: var(--white);
  }
  .hazard:last-child { border-bottom: none; }
  .hazard-icon {
    width: 26px; height: 24px; margin: 0 18px 0 14px; border-radius: 13px 13px 8px 8px;
    background: var(--mascot);
  }
  .hazard-check { position: absolute; right: 20px; top: 5px; }

  .beach { position: absolute; left: 0; bottom: 0; width: 322px; height: 170px; }
  .beach-props {
    position: absolute; left: 30px; bottom: 24px; width: 260px; height: 110px;
    border-radius: 50% 50% 20px 20px / 40% 40% 20px 20px;
    background: radial-gradient(ellipse at 45% 60%, rgba(249,203,62,.55), rgba(242,208,127,0) 70%);
  }
</style>
</head>
<body>
<main class="canvas">

  <!-- Welcome screen -->
  <section class="screen screen--welcome">
    <div class="brand">Quorvy</div>
    <div class="card-ghost"></div>
    <div class="card"></div>
    <h1 class="heading">Welcome to<br>Quorvy!</h1>
    <p class="lede">Real-time beach hazard reports from people just like you</p>
    <button class="cta">GET STARTED</button>
    <svg class="beach" viewBox="0 0 322 170" aria-hidden="true">
      <path d="M94 16 q20 -8 40 0 q20 8 40 0" stroke="var(--wave-line)" stroke-width="4" fill="none" stroke-linecap="round"/>
      <path d="M190 40 q30 -8 60 0" stroke="var(--wave-line)" stroke-width="4" fill="none" stroke-linecap="round"/>
      <path d="M0 60 Q80 40 160 60 T322 52 V170 H0 Z" fill="var(--wave-deep)"/>
      <path d="M0 78 Q90 58 170 80 T322 70 V170 H0 Z" fill="var(--wave-light)"/>
      <path d="M0 92 Q90 74 175 94 T322 84 V170 H0 Z" fill="var(--sand)"/>
    </svg>
    <div class="beach-props" role="img" aria-label="Beach umbrella, beach ball and starfish on the sand"></div>
  </section>

  <!-- Sun safety screen -->
  <section class="screen screen--tips">
    <div class="brand">Quorvy</div>
    <div class="card-ghost"></div>
    <div class="card"></div>
    <h2 class="heading">Sun Safety<br>Tips</h2>
    <div class="tip tip--slip"><span class="tip-label">SLIP</span><div class="tip-art" role="img" aria-label="Jellyfish mascot wearing a shirt"></div></div>
    <div class="tip tip--slop"><span class="tip-label">SLOP</span><div class="tip-art" role="img" aria-label="Jellyfish mascot holding sunscreen"></div></div>
    <div class="tip tip--slap"><span class="tip-label">SLAP</span><div class="tip-art" role="img" aria-label="Jellyfish mascot wearing a hat"></div></div>
    <div class="tip tip--seek"><span class="tip-label">SEEK</span><div class="tip-art" role="img" aria-label="Jellyfish mascot under a beach umbrella"></div></div>
    <div class="tip tip--slide"><span class="tip-label">SLIDE</span><div class="tip-art" role="img" aria-label="Jellyfish mascot wearing sunglasses"></div></div>
    <svg class="beach" viewBox="0 0 322 170" aria-hidden="true">
      <path d="M100 16 q20 -8 40 0 q20 8 40 0" stroke="var(--wave-line)" stroke-width="4" fill="none" stroke-linecap="round"/>
      <path d="M0 60 Q80 40 160 60 T322 52 V170 H0 Z" fill="var(--wave-deep)"/>
      <path d="M0 78 Q90 58 170 80 T322 70 V170 H0 Z" fill="var(--wave-light)"/>
      <path d="M0 92 Q90 74 175 94 T322 84 V170 H0 Z" fill="var(--sand)"/>
    </svg>
    <div class="beach-props" role="img" aria-label="Beach umbrella, beach ball and starfish on the sand"></div>
  </section>

  <!-- Confirm report screen -->
  <section class="screen screen--confirm">
    <div class="brand">Quorvy</div>
    <div class="card-ghost"></div>
    <div class="card"></div>
    <h2 class="heading">Can You<br>Confirm this?</h2>
    <div class="report-art" role="img" aria-label="Doctor jellyfish mascot in front of a radar with jellyfish blips"></div>
    <ul class="hazards">
      <li class="hazard"><span class="hazard-icon" role="img" aria-label="Bluebottle icon"></span>Bluebottle
        <svg class="hazard-check" width="20" height="20" viewBox="0 0 20 20" aria-hidden="true"><circle cx="10" cy="10" r="10" fill="var(--white)"/><path d="M5.5 10.5 l3 3 l6 -6.5" stroke="var(--sky)" stroke-width="2.2" fill="none" stroke-linecap="round" stroke-linejoin="round"/></svg></li>
      <li class="hazard"><span class="hazard-icon" role="img" aria-label="Jellyfish icon"></span>JellyFish
        <svg class="hazard-check" width="20" height="20" viewBox="0 0 20 20" aria-hidden="true"><circle cx="10" cy="10" r="10" fill="var(--white)"/><path d="M5.5 10.5 l3 3 l6 -6.5" stroke="var(--sky)" stroke-width="2.2" fill="none" stroke-linecap="round" stroke-linejoin="round"/></svg></li>
      <li class="hazard"><span class="hazard-icon" role="img" aria-label="Shark icon"></span>Shark
        <svg class="hazard-check" width="20" height="20" viewBox="0 0 20 20" aria-hidden="true"><circle cx="10" cy="10" r="10" fill="var(--white)"/><path d="M5.5 10.5 l3 3 l6 -6.5" stroke="var(--sky)" stroke-width="2.2" fill="none" stroke-linecap="round" stroke-linejoin="round"/></svg></li>
    </ul>
    <svg class="beach" viewBox="0 0 322 170" aria-hidden="true">
      <path d="M96 12 q20 -8 40 0 q20 8 40 0" stroke="var(--wave-line)" stroke-width="4" fill="none" stroke-linecap="round"/>
      <path d="M0 60 Q80 40 160 60 T322 52 V170 H0 Z" fill="var(--wave-deep)"/>
      <path d="M0 78 Q90 58 170 80 T322 70 V170 H0 Z" fill="var(--wave-light)"/>
      <path d="M0 92 Q90 74 175 94 T322 84 V170 H0 Z" fill="var(--sand)"/>
    </svg>
    <div class="beach-props" role="img" aria-label="Beach umbrella, beach ball and starfish on the sand"></div>
  </section>

</main>
</body>
</html>
```